Redesign of an insurance website

Attached is an insurance website that I need to redesign. Currently the website is too dark. I like for example www.brenvalo.com . Could you make the website lighter and change the structure a little so that it is more user friendly?

Industry/Entity Type

Insurance

Number of Pages Required

4 page

```html
<!DOCTYPE html>
<html lang="cs">
<head>
<meta charset="utf-8">
<title>KRYTIMO.CZ – pojištění</title>
<link rel="stylesheet" href="https://fonts.googleapis.com/css2?family=Poppins:wght@400;500;600;700&family=Montserrat:wght@400;500;700&family=Open+Sans:wght@300;400&display=swap">
<style>
:root{
  --blue:#1f7ef0;
  --sky:#66b2f5;
  --orange:#ff7a12;
  --ink:#2a2a2a;
  --muted:#555;
  --grey:#888;
  --line:#e6e6e6;
  --footer:#2d2d2d;
  --footer-bar:#262626;
  --white:#fff;
}
*{margin:0;padding:0;box-sizing:border-box}
html,body{width:917px;height:1200px;overflow:hidden;background:var(--white)}
body{position:relative;font-family:"Montserrat",sans-serif;color:var(--ink)}
.abs{position:absolute}

.site-header{left:0;top:0;width:917px;height:73px;background:var(--white)}
.brand{left:115px;top:24px;font-family:"Poppins",sans-serif;font-weight:700;font-size:21px;color:var(--blue);letter-spacing:.5px}
.user-icon{left:718px;top:24px}
.menu-icon{left:775px;top:26px}

.hero{left:0;top:73px;width:917px;height:449px;background:linear-gradient(180deg,#62aef4,#6cb6f6)}
.hero-art{left:304px;top:24px;width:310px;height:160px;border-radius:4px;background:linear-gradient(180deg,rgba(255,220,140,.85),rgba(255,90,160,.75))}

.social-rail{left:0;top:232px;width:42px;height:132px;background:var(--white);border-right:3px solid var(--orange);box-shadow:0 2px 6px rgba(0,0,0,.15)}
.social-rail span{position:absolute;left:9px;width:26px;height:26px;border-radius:4px;background:var(--blue)}

.quote-card{left:315px;top:188px;width:287px;height:287px;background:var(--white);border-radius:3px;box-shadow:0 4px 14px rgba(0,0,0,.18)}
.tabs{display:flex;height:38px;border-bottom:1px solid var(--line);font-size:8.5px;letter-spacing:1.3px;color:#444}
.tabs span{flex:1;text-align:center;line-height:38px}
.tabs .active{font-weight:700;color:var(--ink);border-bottom:2px solid var(--blue)}
.quote-title{position:absolute;left:0;width:100%;top:56px;text-align:center;font-family:"Poppins",sans-serif;font-weight:400;font-size:18px;color:var(--ink)}
.quote-sub{position:absolute;left:0;width:100%;top:97px;text-align:center;font-size:8px;color:#333}
.products{position:absolute;left:56px;top:118px;width:176px;display:flex;justify-content:space-between}
.product{width:46px;text-align:center;font-size:6.5px;color:var(--orange)}
.product .ring{width:46px;height:46px;border-radius:50%;border:2px solid var(--orange);display:flex;align-items:center;justify-content:center;margin-bottom:5px}
.product.selected{color:var(--blue)}
.product.selected .ring{background:var(--blue);border-color:var(--blue)}
.chev{position:absolute;top:135px;color:#bbb;font-size:14px}
.zip-row{position:absolute;left:40px;top:200px;width:208px;height:30px;border:1px solid #ccc;border-radius:2px;display:flex}
.zip-row .field{flex:1;display:flex;align-items:center;padding-left:8px;font-size:8px;color:#999;gap:6px}
.zip-row .go{width:74px;background:var(--orange);color:var(--white);font-size:8px;display:flex;align-items:center;justify-content:center}
.saved-link{position:absolute;left:0;width:100%;top:245px;text-align:center;font-size:8px;color:var(--blue)}

.why-title{left:0;width:917px;top:542px;text-align:center;font-family:"Poppins",sans-serif;font-weight:400;font-size:20px;color:#777}
.feature{top:583px;width:250px;text-align:center}
.feature .art{width:62px;height:62px;margin:0 auto;border-radius:50%;background:radial-gradient(circle,#dbe9fb,#f2f2f2)}
.feature h3{margin-top:20px;font-family:"Poppins",sans-serif;font-weight:700;font-size:14px;color:var(--orange)}
.feature.blue h3{color:var(--blue)}
.feature p{margin-top:4px;font-size:7.5px;line-height:13.5px;color:#444}

.section-title{font-family:"Open Sans",sans-serif;font-weight:400;font-size:15px;color:#444}
.clock-photo{left:104px;top:829px;width:187px;height:148px;border:1px solid var(--line);background:linear-gradient(135deg,#cfd4d9,#f4f4f4 45%,#9aa0a6)}
.body-copy{font-family:"Open Sans",sans-serif;font-weight:300;font-size:7px;line-height:14.5px;color:#333;text-align:justify}
.cta{left:307px;top:946px;width:93px;height:30px;background:var(--orange);color:var(--white);font-family:"Open Sans",sans-serif;font-size:11px;display:flex;align-items:center;justify-content:center}

.site-footer{left:0;top:1009px;width:917px;height:144px;background:var(--footer)}
.footer-brand{left:118px;top:1040px;font-family:"Poppins",sans-serif;font-weight:700;font-size:19px;color:var(--blue);letter-spacing:.5px}
.email-field{left:118px;top:1077px;width:177px;height:24px;background:var(--white);font-size:8px;color:#999;padding-left:8px;line-height:24px}
.pill{height:22px;border-radius:11px;color:var(--white);font-weight:700;font-size:7px;display:flex;align-items:center;justify-content:center;letter-spacing:.3px}
.pill.blue{left:166px;top:1112px;width:80px;background:var(--blue)}
.pill.orange{left:418px;top:1112px;width:80px;background:var(--orange)}
.foot-h{font-family:"Poppins",sans-serif;font-weight:600;font-size:13px;color:var(--white)}
.foot-text{left:340px;top:1059px;width:236px;text-align:center;font-size:7.5px;line-height:14px;color:#ddd}
.contact-line{left:670px;font-size:7px;color:var(--white);display:flex;align-items:center;gap:6px}
.social-circles{left:669px;top:1113px;display:flex;gap:6px}
.social-circles span{width:23px;height:23px;border-radius:50%;border:1.5px solid var(--white)}
.footer-bar{left:0;top:1153px;width:917px;height:47px;background:var(--footer-bar);border-top:1px solid #3a3a3a}
.copyright{left:115px;top:1172px;font-size:7.5px;color:#ccc}
.foot-nav{left:560px;top:1173px;display:flex;gap:22px;font-weight:700;font-size:7.5px;color:var(--white)}
</style>
</head>
<body>

<header class="abs site-header">
  <div class="abs brand">KRYTIMO.CZ</div>
  <svg class="abs user-icon" width="24" height="24" viewBox="0 0 24 24" fill="none" stroke="#ff7a12" stroke-width="1.8"><circle cx="12" cy="8" r="5"/><path d="M2 22c0-5 4.5-8 10-8s10 3 10 8z"/></svg>
  <svg class="abs menu-icon" width="27" height="20" viewBox="0 0 27 20" stroke="#1f7ef0" stroke-width="2.6"><path d="M0 2h27M0 10h27M0 18h27"/></svg>
</header>

<section class="abs hero"></section>
<div class="abs hero-art" role="img" aria-label="Illustration of an open yellow and pink umbrella sheltering the quote form from the rain"></div>

<aside class="abs social-rail" aria-label="Social links">
  <span style="top:13px"></span>
  <span style="top:53px"></span>
  <span style="top:93px"></span>
</aside>

<section class="abs quote-card">
  <nav class="tabs">
    <span class="active">QUOTE</span><span>PAYMENTS</span><span>CLAIMS</span><span>AGENTS</span>
  </nav>
  <h1 class="quote-title">Get a Qoute</h1>
  <p class="quote-sub">Select a product to start a quote</p>
  <span class="chev" style="left:42px">&#8249;</span>
  <span class="chev" style="left:240px">&#8250;</span>
  <div class="products">
    <div class="product"><div class="ring">
      <svg width="26" height="24" viewBox="0 0 26 24" fill="none" stroke="#ff7a12" stroke-width="1.6"><path d="M2 12L13 2l11 10M5 10v12h16V10M10 22v-7h6v7"/></svg>
    </div>Home</div>
    <div class="product selected"><div class="ring">
      <svg width="30" height="18" viewBox="0 0 30 18" fill="none" stroke="#fff" stroke-width="1.6"><path d="M2 12V9l4-1 4-5h10l4 5 4 1v3z"/><circle cx="8" cy="13" r="2.5"/><circle cx="22" cy="13" r="2.5"/></svg>
    </div>Auto</div>
    <div class="product"><div class="ring">
      <svg width="26" height="26" viewBox="0 0 26 26" fill="none" stroke="#ff7a12" stroke-width="1.6"><path d="M22 3l-7 7-10-3-2 2 8 5-4 5H4l-1 2 4 2 2 4 2-1v-3l5-4 5 8 2-2-3-10 7-7c1-2 0-3-2-2z"/></svg>
    </div>Air Plane</div>
  </div>
  <div class="zip-row">
    <div class="field">
      <svg width="8" height="11" viewBox="0 0 8 11"><path d="M4 0a4 4 0 0 1 4 4c0 3-4 7-4 7S0 7 0 4a4 4 0 0 1 4-4z" fill="#ff7a12"/><circle cx="4" cy="4" r="1.4" fill="#fff"/></svg>
      ZIP Code
    </div>
    <div class="go">Start Qoute</div>
  </div>
  <p class="saved-link">Continue a saved quote</p>
</section>

<h2 class="abs why-title">Why KRYTIMO?</h2>

<div class="abs feature" style="left:81px">
  <div class="art" role="img" aria-label="Icon of a money bag beside stacked coins"></div>
  <h3>Perspiciatis Unde Omnis</h3>
  <p>At vero eos et accusamus et iusto odio dignissimos ducimus qui blanditiis praesentium voluptatum atque corrupti quos dolores et quas molestias.</p>
</div>
<div class="abs feature blue" style="left:333px">
  <div class="art" role="img" aria-label="Icon of two phones exchanging contact details"></div>
  <h3>Sed Ut Unde Omnis</h3>
  <p>Vero eos et accusamus et iusto odio dignissimos ducimus qui blanditiis praesentium atque corrupti quos dolores et quas molestias excepturi.</p>
</div>
<div class="abs feature" style="left:585px">
  <div class="art" role="img" aria-label="Icon of a light bulb shaped like a rocket"></div>
  <h3>Iste Natus Error</h3>
  <p>Accusamus et iusto odio dignissimos ducimus qui blanditiis praesentium voluptatum atque corrupti quos quas molestias excepturi.</p>
</div>

<h2 class="abs section-title" style="left:106px;top:782px">Uzavřeli jste v minulosti nevýhodnou pojistku? Zbavte se jí!</h2>
<div class="abs clock-photo" role="img" aria-label="Photo of a wall clock face with the words Čas pro lepší pojištění"></div>
<p class="abs body-copy" style="left:307px;top:826px;width:194px">Máte pocit, že za stávající pojištění platíte příliš? A že za své peníze dostáváte méně služeb než druzí? Pojďte s tím něco udělat! S námi najdete tu nejvýhodnější nabídku na trhu a navíc vám poradíme, jak se nejsnáze zbavit starého nevýhodného pojištění. Stačí kliknout na tlačítko UŠETŘIT a můžete se vydat na cestu k lepšímu a levnějšímu pojištění.</p>
<div class="abs cta">CHCI UŠETŘIT</div>

<h2 class="abs section-title" style="left:543px;top:784px">Jak to funguje</h2>
<p class="abs body-copy" style="left:543px;top:823px;width:273px">Portál Krytimo.cz vám otevírá cestu k těm nejvýhodnějším pojistkám na trhu. Srovnávame nabídky všech pojišťoven a pomocí unikátního algoritmu vám z nich vybereme tu nejvýhodnější. Zařídíme pro vás všechny druhy pojištění včetně povinného ručení, pojištění domácnosti či osobního pojištění. A hlavně – všechno můžete vyřešit snadno online, aniž byste museli někam chodit. S námi tak ušetříte peníze, čas, nervy, a dokonce i obuv :)</p>

<footer class="abs site-footer"></footer>
<div class="abs footer-brand">KRYTIMO.CZ</div>
<div class="abs email-field">Your email</div>
<div class="abs pill blue">SUBSCRIBE</div>

<h3 class="abs foot-h" style="left:437px;top:1035px">About</h3>
<p class="abs foot-text">Eos et accusamus et iusto odio dignissimos ducimus qui blanditiis praesentium voluptatum deleniti atque. At vero eos et accusamus iusto odio dignissimos.</p>
<div class="abs pill orange">GET QUOTE</div>

<h3 class="abs foot-h" style="left:672px;top:1030px">Contact Us</h3>
<div class="abs contact-line" style="top:1068px">
  <svg width="10" height="8" viewBox="0 0 10 8" fill="none" stroke="#fff"><rect x=".5" y=".5" width="9" height="7"/><path d="M.5 .5l4.5 4 4.5-4"/></svg>INFO@KRYTIMO.CZ
</div>
<div class="abs contact-line" style="top:1085px">
  <svg width="10" height="10" viewBox="0 0 10 10" fill="none" stroke="#fff"><circle cx="5" cy="5" r="4.3"/><circle cx="5" cy="5" r="1.8"/></svg>+41-41-555-0190
</div>
<div class="abs social-circles" aria-label="Social links"><span></span><span></span><span></span></div>

<div class="abs footer-bar"></div>
<div class="abs copyright">© KRYTIMO | 2017</div>
<nav class="abs foot-nav"><span>HOME</span><span>SERVICE</span><span>ABOUT</span><span>BLOG</span><span>CONTACT</span></nav>

</body>
</html>
```